Verpackungsdesign für Wellness- und Saunaprodukte
Zielgruppe
Brisavo ist ein junges Start-Up, das sich auf Wellness- und Saunaprodukte spezialisiert hat. Unsere Zielgruppe besteht zu beinahe gleichen Teilen aus männlichen und weiblichen Personen zwischen 30 und 60 Jahren. Unsere Produkte befinden sich eher im mittel- bis höherpreisigen Segment, daher streben wir ein hochwertiges Design für unsere Verpackungen an. Unsere Produktpalette reicht von Mentholkristallen, Saunaaufgüssen, bis hin zu Textilien für den Wellnessbereich und soll dementsprechend Menschen ansprechen, die sich einen gewissen Luxus im Alltag auch gönnen.
Aufgabenstellung
Inspiriert von der skandinavischen Sauna Kultur, möchten wir Momente der Erholung und
Entspannung in den Alltag unserer Kunden bringen. Die Geschichte des Saunierens ist eng mit der skandinavischen Kultur verbunden und skandinavische Stilelemente sind zeitgemäß und sprechen ein breites Publikum an. Das Design muss auf Dosen/Tiegel , Karton Verpackungen und Flaschen verschiedener Größen adaptierbar sein (siehe Bild im Anhang).
40g Tiegel(transparent) Höhe 40mm Durchmesser 60mm (ohne Deckel Silber gebürstet)
100g Tiegel(transparent) Höhe 53mm Durchmesser 71mm (ohne Deckel Silber gebürstet)
200g Tiegel(transparent) Höhe 65mm Durchmesser 90mm (ohne Deckel Silber gebürstet)
Karton Verpackung 124,5x49x49mm
Karton Verpackung 100x100x100mm
Flaschenetikett 134x67mm (Braunglas, schwarzer Deckel)
Es soll ein passendes Keyvisual erstellt werden.
Im Anhang sieht man die Verpackungen, Dosen, Flaschen sowie unsere ersten Design Entwürfe (an diese Anordnung der Elemente kann sich der Designer orientieren ). Das Logo bleibt wie gegeben. Das Produkt für die Tiegel soll Mentholkristalle sein.

```html
<!DOCTYPE html>
<html lang="de">
<head>
<meta charset="utf-8">
<title>Brisavo – Verpackungsdesign Wellness &amp; Sauna</title>
<link rel="stylesheet" href="https://fonts.googleapis.com/css2?family=Montserrat:wght@400;600;700&display=swap">
<style>
  :root {
    --canvas: #e4e4e4;
    --label-ground: #ececec;
    --pattern-tone: #e2e2e2;
    --panel: #ffffff;
    --ink: #1e1e1e;
    --fichte: #7f9b6b;
    --menthol: #3d7c76;
    --granat: #a2383b;
  }
  html, body {
    margin: 0;
    width: 1200px;
    height: 603px;
    overflow: hidden;
    background: var(--canvas);
    font-family: "Montserrat", sans-serif;
  }
  .label {
    position: absolute;
    background: var(--label-ground);
    box-shadow: 0 2px 6px rgba(0,0,0,.08);
    overflow: hidden;
  }
  .label__pattern {
    position: absolute;
    inset: 0;
    background: linear-gradient(180deg, var(--pattern-tone), #efefef);
  }
  .label__band {
    position: absolute;
    left: 0; right: 0; bottom: 0;
  }
  .brand-plate {
    position: absolute;
    left: 50%;
    transform: translateX(-50%);
    display: flex;
    align-items: flex-end;
    justify-content: center;
    color: #fff;
    font-weight: 400;
    letter-spacing: .02em;
  }
  .title-panel {
    position: absolute;
    background: var(--panel);
    display: flex;
    flex-direction: column;
    align-items: center;
    justify-content: center;
    text-align: center;
  }
  .title-panel__name {
    margin: 0;
    font-weight: 700;
    color: var(--ink);
    letter-spacing: .08em;
    line-height: 1.2;
  }
  .title-panel__rule {
    width: 18px;
    height: 1px;
    background: var(--ink);
    margin: 5px 0;
  }
  .title-panel__use {
    margin: 0;
    font-weight: 400;
    letter-spacing: .08em;
    line-height: 1.35;
  }

  /* Karton Nordische Fichte */
  .carton { left: 172px; top: 161px; width: 127px; height: 324px; }
  .carton .brand-plate { top: 0; width: 29px; height: 43px; font-size: 5px; padding-bottom: 4px; box-sizing: border-box; background: var(--fichte); }
  .carton .title-panel { left: 12px; right: 12px; top: 134px; height: 84px; }
  .carton .title-panel__name { font-size: 12px; }
  .carton .title-panel__use { font-size: 5.5px; color: var(--fichte); margin-top: 10px; }
  .carton .title-panel__rule { margin: 5px 0 0; }
  .carton .label__band { height: 5px; background: var(--fichte); }

  /* Flaschenetikett Nordische Fichte */
  .bottle { left: 315px; top: 306px; width: 104px; height: 170px; }
  .bottle .brand-plate { top: 14px; width: 20px; height: 26px; font-size: 4px; padding-bottom: 3px; box-sizing: border-box; background: var(--fichte); }
  .bottle .title-panel { left: 8px; right: 8px; top: 61px; height: 79px; }
  .bottle .title-panel__name { font-size: 11px; }
  .bottle .title-panel__use { font-size: 5px; color: var(--fichte); }
  .bottle .label__band { height: 7px; background: var(--fichte); }

  /* Tiegeletikett Mentholkristalle */
  .jar-menthol { left: 460px; top: 385px; width: 220px; height: 95px; }
  .jar-menthol .brand-plate { top: 6px; width: 18px; height: 23px; font-size: 3.6px; padding-bottom: 3px; box-sizing: border-box; background: var(--menthol); }
  .jar-menthol .title-panel { left: 36px; width: 150px; top: 37px; height: 40px; }
  .jar-menthol .title-panel__name { font-size: 11px; }
  .jar-menthol .title-panel__use { font-size: 5px; color: var(--menthol); }
  .jar-menthol .title-panel__rule { margin: 4px 0; }
  .jar-menthol .label__band { bottom: 10px; height: 5px; background: var(--menthol); }

  /* Tiegeletikett Granatapfel */
  .jar-granat { left: 702px; top: 385px; width: 220px; height: 95px; }
  .jar-granat .brand-plate { top: 6px; width: 18px; height: 23px; font-size: 3.6px; padding-bottom: 3px; box-sizing: border-box; background: var(--granat); }
  .jar-granat .title-panel { left: 41px; width: 139px; top: 37px; height: 40px; }
  .jar-granat .title-panel__name { font-size: 11px; }
  .jar-granat .title-panel__use { font-size: 4.6px; color: var(--granat); }
  .jar-granat .title-panel__rule { margin: 4px 0; }
  .jar-granat .label__band { bottom: 10px; height: 5px; background: var(--granat); }
</style>
</head>
<body>
  <section class="label carton">
    <div class="label__pattern" role="img" aria-label="Helles graues Ornamentmuster aus verschlungenen Linien"></div>
    <div class="brand-plate">Brisavo</div>
    <div class="title-panel">
      <h2 class="title-panel__name">NORDISCHE<br>FICHTE</h2>
      <div class="title-panel__rule"></div>
      <p class="title-panel__use">AUFGUSS<br>FÜR DIE SAUNA</p>
    </div>
    <div class="label__band"></div>
  </section>

  <section class="label bottle">
    <div class="label__pattern" role="img" aria-label="Helles graues Ornamentmuster aus verschlungenen Linien"></div>
    <div class="brand-plate">Brisavo</div>
    <div class="title-panel">
      <h2 class="title-panel__name">NORDISCHE<br>FICHTE</h2>
      <div class="title-panel__rule"></div>
      <p class="title-panel__use">AUFGUSS<br>FÜR DIE SAUNA</p>
    </div>
    <div class="label__band"></div>
  </section>

  <section class="label jar-menthol">
    <div class="label__pattern" role="img" aria-label="Helles graues Ornamentmuster aus verschlungenen Linien"></div>
    <div class="brand-plate">Brisavo</div>
    <div class="title-panel">
      <h2 class="title-panel__name">MENTHOLKRISTALLE</h2>
      <div class="title-panel__rule"></div>
      <p class="title-panel__use">FÜR DIE SAUNA</p>
    </div>
    <div class="label__band"></div>
  </section>

  <section class="label jar-granat">
    <div class="label__pattern" role="img" aria-label="Helles graues Ornamentmuster aus verschlungenen Linien"></div>
    <div class="brand-plate">Brisavo</div>
    <div class="title-panel">
      <h2 class="title-panel__name">GRANATAPFEL</h2>
      <div class="title-panel__rule"></div>
      <p class="title-panel__use">MEERSALZPEELING FÜR DEN KÖRPER</p>
    </div>
    <div class="label__band"></div>
  </section>
</body>
</html>
```